Email Newsletter Header/Banner

We are an Australian Real Estate investment company that require a header for our email newsletter. Dimensions 790px by 180px.

Header must include both our website logos
http://www.kovelplan.com.au
http://kovelproperty.com.au

We want the header to have a human or community feel. No corporate or business look. Clean modern design
Updates

Please only use the logo of KOVEL PlanĀ http://www.kovelplan.com.au

Target Market(s)

Real Estate Investors

Industry/Entity Type

Investment

Requirements
Must have
• Community or human feel

```html
<!DOCTYPE html>
<html lang="en">
<head>
<meta charset="utf-8">
<title>KOVEL Plan Newsletter Header</title>
<link rel="stylesheet" href="https://fonts.googleapis.com/css2?family=Open+Sans:ital,wght@0,700;1,400&display=swap">
<style>
  :root {
    --page: #ffffff;
    --brand-blue: #2f86c6;
    --brand-blue-deep: #1f6fb0;
    --sky-light: #e9eef3;
    --paper: #ffffff;
    --mist: #e4e6e8;
    --slate: #5a5a5a;
    --slate-dark: #454545;
    --ink: #1c1c1c;
  }
  * { margin: 0; padding: 0; box-sizing: border-box; }
  html, body {
    width: 1200px;
    height: 278px;
    overflow: hidden;
    background: var(--page);
  }
  .canvas {
    position: relative;
    width: 1200px;
    height: 278px;
  }
  .header-banner {
    position: absolute;
    left: 90px;
    top: 51px;
    width: 1029px;
    height: 174px;
    overflow: hidden;
    box-shadow: 0 2px 8px rgba(0, 0, 0, 0.35);
  }
  .banner-art {
    position: absolute;
    inset: 0;
    width: 100%;
    height: 100%;
  }
  .issue-line {
    font-family: "Open Sans", Arial, sans-serif;
    font-style: italic;
    font-weight: 400;
    font-size: 12px;
    letter-spacing: 1px;
    fill: var(--brand-blue);
  }
  .brand-lockup {
    position: absolute;
    left: 222px;
    top: 50px;
    display: flex;
    align-items: center;
    gap: 12px;
  }
  .brand-mark {
    width: 46px;
    height: 46px;
    background: var(--brand-blue);
  }
  .brand-name {
    font-family: "Open Sans", Arial, sans-serif;
    font-weight: 700;
    font-size: 66px;
    line-height: 1;
    letter-spacing: -1px;
    color: var(--ink);
  }
</style>
</head>
<body>
<div class="canvas">
  <header class="header-banner">
    <svg class="banner-art" viewBox="0 0 1029 174" aria-hidden="true">
      <defs>
        <linearGradient id="paperFill" x1="0" y1="0" x2="0" y2="1">
          <stop offset="0" stop-color="var(--paper)"/>
          <stop offset="1" stop-color="var(--mist)"/>
        </linearGradient>
        <linearGradient id="blueFill" x1="0" y1="0" x2="1" y2="1">
          <stop offset="0" stop-color="var(--brand-blue)"/>
          <stop offset="1" stop-color="var(--brand-blue-deep)"/>
        </linearGradient>
        <linearGradient id="slateFill" x1="0" y1="0" x2="1" y2="0">
          <stop offset="0" stop-color="var(--slate-dark)"/>
          <stop offset="1" stop-color="var(--slate)"/>
        </linearGradient>
        <path id="issueCurve" d="M232,160 C400,137 580,129 770,131"/>
      </defs>

      <rect class="banner-base" width="1029" height="174" fill="url(#paperFill)"/>
      <path class="corner-sky" d="M0,0 H236 C150,22 60,70 0,112 Z" fill="url(#blueFill)"/>
      <path class="corner-haze" d="M0,112 C60,70 150,22 236,0 H270 C170,30 80,90 0,150 Z" fill="var(--sky-light)" opacity="0.7"/>
      <path class="base-swoosh" d="M110,174 C380,148 640,148 860,174 Z" fill="url(#blueFill)"/>
      <path class="base-swoosh-edge" d="M110,174 C380,148 640,148 860,174" fill="none" stroke="var(--paper)" stroke-width="2"/>
      <path class="side-slate" d="M1029,0 H935 C850,30 795,100 772,174 H1029 Z" fill="url(#slateFill)"/>

      <text class="issue-line">
        <textPath href="#issueCurve">Newsletter for Australian Real Estate Investment company- Issue no 1</textPath>
      </text>
    </svg>

    <div class="brand-lockup">
      <span class="brand-mark"></span>
      <h1 class="brand-name">kovelplan.com</h1>
    </div>
  </header>
</div>
</body>
</html>
```